Traffic product supplier - Temporary Raised Pavement Markers

We need a flyer design that will grab the customer's eye to the product (TRPMs) and entice curiosity to the business. Showing 1 product but promoting other products. The following information should be included:
- Logo (attached)
- Sale Product image (Temporary Road Pavement Marker AKA Press and Holds)
- Product wording (attached word document)

Happy for you to add/amend wording for grammatical purpose and other images that show it is a sale flyer.

Background on KLV - We are a thermoplastic manufacturer for road markings and traffic product supplier. KLV specializes in producing high quality hotmelt thermoplastic that meet Australian Standard AS4049.2. We are able to produce other specifications as required by the customer.

Would like the colour scheme to be similar to the logo.

If you need more information let me know.

Target Market(s)

Asphalt industry / road builders

Font styles to use
Serif
Sans Serif

Requirements
Must have
• - Kelvoro Lane Ventures (My company name)
- Contact details:
- 02 8417 2530
- marcus.t@klvsupplyco.com.au
- info@klvsupplyco.com.au
-www.klvmtq.com

- Attached images.
-Title (Temporary Road Pavement Markers)

```html
<!DOCTYPE html>
<html lang="en">
<head>
<meta charset="utf-8">
<title>Temporary Road Pavement Marker – Kelvoro Lane Ventures</title>
<link rel="stylesheet" href="https://fonts.googleapis.com/css2?family=Open+Sans:ital,wght@0,400;0,600;0,700;1,400&family=Oswald:wght@700&display=swap">
<style>
  :root{
    --blue:#1b6fb8;
    --blue-dark:#0f4f8c;
    --ink:#333a40;
    --white:#ffffff;
    --list-bg:#1f73bd;
    --photo-top:#6b7868;
    --photo-bottom:#45494b;
  }
  *{margin:0;padding:0;box-sizing:border-box}
  html,body{width:849px;height:1200px;overflow:hidden;background:var(--white)}
  body{font-family:"Open Sans",Arial,sans-serif;color:var(--ink);position:relative}

  .hero{position:absolute;left:0;top:0;width:849px;height:360px;
    background:linear-gradient(180deg,var(--photo-top) 0%,var(--photo-bottom) 100%)}
  .title{position:absolute;left:40px;top:192px;width:600px;font-family:"Oswald",Impact,sans-serif;
    font-weight:700;font-size:46px;line-height:1.1;color:var(--white);text-transform:uppercase;
    text-shadow:0 2px 6px rgba(0,0,0,.55)}

  .section{position:absolute;left:40px;width:520px}
  .section h2{color:var(--blue);font-size:19px;font-weight:700;margin-bottom:8px}
  .section p{font-size:14px;line-height:1.5}
  .desc{top:385px}
  .product{top:515px}

  .markers{position:absolute;right:40px;top:560px;width:215px}
  .marker{height:95px;margin-bottom:30px;border-radius:4px}
  .marker.white{background:linear-gradient(180deg,#f4f4f4,#c9c9c9);border-top:10px solid #c0392b}
  .marker.yellow{background:linear-gradient(180deg,#f2b01e,#c98a0c)}
  .marker.clear{background:linear-gradient(180deg,#eef0f2,#b9bec3)}

  .specs{position:absolute;left:28px;top:730px;width:530px;background:var(--list-bg);color:var(--white);
    padding:20px 22px;list-style:none;font-size:14px;line-height:1.75}
  .specs li{display:flex;align-items:center;gap:10px}
  .specs li::before{content:"";width:11px;height:11px;border:2px solid var(--white);flex:none}

  .brand{position:absolute;left:40px;top:945px;width:240px}
  .brand-mark{display:flex;align-items:center;gap:12px;height:110px;background:var(--blue);padding:0 22px}
  .brand-mark .sq{width:34px;height:34px;background:var(--white)}
  .brand-mark span{font-size:52px;font-weight:700;color:var(--white)}
  .brand small{display:block;font-size:9px;margin-top:6px;font-style:italic}

  .contact{position:absolute;left:300px;top:955px;font-size:15px;line-height:1.45}
  .contact strong{display:block;font-size:17px;color:var(--blue-dark);text-transform:uppercase}
  .contact .phone{font-size:20px;font-weight:700;color:var(--blue-dark)}

  .web{position:absolute;right:40px;top:1110px;font-size:26px;font-weight:700;color:var(--blue)}
  .band{position:absolute;left:0;bottom:0;width:849px;height:32px;background:var(--blue)}
</style>
</head>
<body>
  <div class="hero" role="img" aria-label="Photo of a newly sealed country road running between green verges"></div>
  <h1 class="title">Temporary Road Pavement Marker AKA Press and Holds</h1>

  <section class="section desc">
    <h2>Use/General Description:</h2>
    <p>Temporary road pavement markers, also known as stick 'n' stomps, are a great short term solution to mark asphalt and pavements before permanent line marking takes place. They provide a way to delineate lanes and edges before the permanent longitudinal line marking process takes place.</p>
  </section>

  <section class="section product">
    <h2>Product description:</h2>
    <p>TRPMs or stick 'n' stomps are available in yellow or white and come with a Class 1A reflective strip applied to tough high impact plastic. They are an economical solution for making newly laid roads safer. An easy to remove clear cover protects the reflective film during sealing and is easily ripped off afterwards.</p>
  </section>

  <div class="markers">
    <div class="marker white" role="img" aria-label="White temporary pavement marker with red reflective strip"></div>
    <div class="marker yellow" role="img" aria-label="Yellow temporary pavement marker"></div>
    <div class="marker clear" role="img" aria-label="White temporary pavement marker with clear cover"></div>
  </div>

  <ul class="specs">
    <li>Dimensions: 100 mm long x 50 mm high x 25 mm wide</li>
    <li>Double sided Class 1A Reflective</li>
    <li>Clear cover for reflective protection</li>
    <li>Available in all white, and red (reflective strip) and white, all yellow and all blue</li>
  </ul>

  <div class="brand">
    <div class="brand-mark"><div class="sq"></div><span>KLV</span></div>
    <small>"Creating a Safe Environment for All Road Users"</small>
  </div>

  <div class="contact">
    <strong>Kelvoro Lane Ventures</strong>
    <div class="phone">02 8417 2530</div>
    <div>marcus.t@klvsupplyco.com.au</div>
    <div>info@klvsupplyco.com.au</div>
  </div>

  <div class="web">www.klvmtq.com</div>
  <div class="band"></div>
</body>
</html>
```